Letterhead & logo design project

We need a letterhead for a new company called Brackenwold Ltd a firm of Chartered Accountants and Chartered Tax Advisers based in Pangbourne, Berkshire
Updates
Please include the following:
Chartered Accountants and Chartered Tax Advisers
Industry/Entity Type
It Company
Requirements
Must have
- Must have director's name at the bottom of the letterhead. Must also contain some wording at the bottom of the page to be provided by the NPRFA at a later date

```html
<!DOCTYPE html>
<html lang="en">
<head>
<meta charset="utf-8">
<title>Brackenwold Ltd — Letterhead</title>
<link rel="stylesheet" href="https://fonts.googleapis.com/css2?family=Cinzel:wght@500;700&family=Josefin+Sans:wght@300;400;600&display=swap">
<style>
  :root {
    --backdrop: #dcdcdc;
    --paper: #f4f4f4;
    --brand-red: #b5121b;
    --ink: #2a2a2a;
    --ink-soft: #7a7a7a;
    --rule: #555555;
  }
  * { box-sizing: border-box; margin: 0; padding: 0; }
  html, body {
    width: 1200px;
    height: 968px;
    overflow: hidden;
    background: var(--backdrop);
  }
  .letterhead {
    position: absolute;
    left: 290px;
    top: 44px;
    width: 620px;
    height: 880px;
    background: var(--paper);
    box-shadow: 0 6px 18px rgba(0,0,0,0.18);
    font-family: "Josefin Sans", sans-serif;
    color: var(--ink);
  }
  .brand {
    position: absolute;
    top: 40px;
    left: 0;
    right: 0;
    text-align: center;
  }
  .brand-square {
    display: block;
    width: 38px;
    height: 38px;
    margin: 0 auto 8px;
    background: var(--brand-red);
  }
  .brand-name {
    font-family: "Cinzel", serif;
    font-weight: 700;
    font-size: 22px;
    letter-spacing: 0.5px;
    color: var(--ink);
  }
  .brand-tagline {
    margin-top: 4px;
    font-size: 8.5px;
    line-height: 1.35;
    letter-spacing: 1px;
    text-transform: uppercase;
    color: var(--ink-soft);
    font-weight: 300;
  }
  .membership {
    position: absolute;
    left: 34px;
    bottom: 50px;
    display: flex;
    align-items: center;
    gap: 8px;
  }
  .membership-square {
    width: 30px;
    height: 30px;
    background: var(--brand-red);
  }
  .membership-name {
    font-size: 13px;
    font-weight: 400;
    letter-spacing: 0.5px;
    color: var(--ink);
  }
  .signature-block {
    position: absolute;
    right: 34px;
    bottom: 44px;
    width: 210px;
    text-align: right;
    border-top: 1px solid var(--rule);
    padding-top: 6px;
    font-size: 9.5px;
    line-height: 1.45;
  }
  .director-name {
    font-weight: 600;
    text-transform: uppercase;
    letter-spacing: 0.3px;
  }
  .director-role { color: var(--ink); margin-bottom: 4px; }
  .contact-address,
  .contact-lines { text-align: left; color: var(--ink); white-space: nowrap; }
  .contact-label { color: var(--brand-red); font-weight: 600; }
</style>
</head>
<body>
  <main class="letterhead">
    <header class="brand">
      <span class="brand-square" aria-hidden="true"></span>
      <h1 class="brand-name">Brackenwold Ltd.</h1>
      <p class="brand-tagline">Chartered Accountants<br>and Chartered Tax Advisers</p>
    </header>

    <aside class="membership">
      <span class="membership-square" aria-hidden="true"></span>
      <span class="membership-name">NPRFA</span>
    </aside>

    <footer class="signature-block">
      <p class="director-name">Helen Brackenwold</p>
      <p class="director-role">Director</p>
      <p class="contact-address">BRACKENWOLD Ltd, Fernbury, FB4 2LW</p>
      <p class="contact-lines">
        <span class="contact-label">Tel:</span> 01632 960 418 &middot;
        <span class="contact-label">Fax:</span> 01632 960 418
      </p>
    </footer>
  </main>
</body>
</html>
```